Home page makeover

Take my existing home page, www.maplecrestledger.com and redesign layout to look more current considering today's touch design prevalence.
Reuse existing elements or suggest improved ones if available.
I generally have average CSS and HTML skills using div containers, defining lists and using columns to create the code to support the layout.
Updates
Just wanted to send out a quick message to thank all of you for your submissions. Many of you offered nice designs, but unfortunately could only choose one.
Target Market(s)
Generally targeting individuals with some assets for retirement. Basically your average working professional or business owner.
Industry/Entity Type
It Support
Look and feel
Each slider illustrates characteristics of the customer's brand and the style your logo design should communicate.

```html
<!DOCTYPE html>
<html lang="en">
<head>
<meta charset="utf-8">
<title>Maplecrest Ledger – Home</title>
<link href="https://fonts.googleapis.com/css2?family=Roboto:ital,wght@0,400;0,500;0,700;1,400&display=swap" rel="stylesheet">
<style>
:root{
  --green-dark:#0b5d1e;
  --green-mid:#2f7d1c;
  --green-light:#9dcd45;
  --green-btn:#8cc63f;
  --text:#555;
  --text-dark:#333;
  --line:#cfcfcf;
  --card-bg:#f6f6f6;
  --footer:#3b3b3b;
  --white:#fff;
}
*{margin:0;padding:0;box-sizing:border-box}
html,body{width:946px;height:1200px;overflow:hidden}
body{font-family:'Roboto',sans-serif;color:var(--text);background:#f2f2f2;position:relative}
.abs{position:absolute}
.green-band{left:0;top:389px;width:946px;height:730px;background:var(--green-light)}
.page{left:125px;top:0;width:697px;height:1119px;background:var(--white);box-shadow:0 0 6px rgba(0,0,0,.2)}
.brand{left:132px;top:22px}
.brand-name{font-size:27px;font-weight:700;color:var(--green-dark);letter-spacing:.5px;display:flex;align-items:center;gap:8px}
.brand-mark{width:22px;height:22px;background:var(--green-dark)}
.brand-tag{font-size:12px;color:var(--text-dark);margin:8px 0 0 30px;letter-spacing:.3px}
.auth{left:613px;top:13px;width:110px;height:30px;background:var(--green-btn);color:var(--green-dark);font-size:10.5px;font-weight:500;display:flex;align-items:center;justify-content:center}
.social{left:735px;top:16px;display:flex;gap:6px}
.social span{width:23px;height:23px;border-radius:4px;display:block}
.nav{right:131px;top:74px;display:flex;font-size:10.5px;color:var(--text-dark);height:25px;align-items:center}
.nav a{text-decoration:none;color:inherit;padding:0 10px;height:25px;line-height:25px}
.nav a.active{background:var(--green-dark);color:var(--white);padding:0 9px}
.slider{left:132px;top:110px;width:683px;height:279px;background:#e9e9e9;padding:3px}
.slider-photo{width:100%;height:100%;background:linear-gradient(90deg,#c9a98a 0%,#e8d7c4 35%,#8fb2c9 60%,#cfa36f 80%,#e5d6c2 100%)}
.promo{left:506px;top:274px;width:291px;height:98px;background:var(--green-btn);opacity:.95;padding:6px 10px;box-shadow:0 2px 4px rgba(0,0,0,.3)}
.promo h2{color:var(--white);font-size:26px;font-weight:500;letter-spacing:.5px}
.promo p{color:var(--green-dark);font-size:14.5px;font-weight:700;margin-top:2px}
.promo b{color:var(--white)}
.dots{left:145px;top:361px;display:flex;gap:4px}
.dots span{width:12px;height:12px;border-radius:50%;background:#555}
.dots span:first-child{background:#222}
.card{top:408px;width:218px;height:232px;background:var(--card-bg);border:1px solid #ddd;padding:10px 14px}
.card h3{font-size:18px;font-weight:500;color:var(--green-dark);letter-spacing:.3px}
.card .img{width:188px;height:106px;margin-top:6px;border:2px solid #fff}
.card p{font-size:10px;line-height:14.5px;margin-top:10px}
.card a{display:block;margin-top:7px;font-size:10px;font-weight:500;color:var(--green-dark);text-decoration:none}
.card.active{background:var(--green-dark);border-color:var(--green-dark);box-shadow:0 4px 5px rgba(0,0,0,.3)}
.card.active h3,.card.active p{color:var(--white)}
.card.active a{color:var(--green-light)}
.rule{left:132px;width:683px;height:1px;background:var(--line)}
h2.section{font-size:15px;font-weight:500;color:var(--green-dark);letter-spacing:.3px}
.welcome-text{left:132px;top:697px;width:395px;font-size:10px;line-height:16.7px}
.btn{height:27px;background:var(--green-btn);color:var(--green-dark);font-size:10px;font-weight:500;display:flex;align-items:center;justify-content:center;width:80px}
.video{left:538px;top:699px;width:275px;height:190px;background:#111}
.video-frame{left:35px;top:18px;width:206px;height:153px;background:linear-gradient(160deg,#d8d8d8,#6b6b6b 60%,#2a2a2a)}
.video-bar{left:0;bottom:0;width:100%;height:17px;background:#1e1e1e;border-top:3px solid #444}
.features{left:132px;top:952px;width:433px;list-style:none;font-size:10px;line-height:14.7px}
.features li{display:flex;gap:9px;margin-bottom:6px}
.features svg{flex:none;margin-top:2px}
.quotes{left:596px;top:950px;width:217px;height:121px;background:var(--card-bg);border:1px solid #ddd;padding:14px 12px 0 12px;font-size:9.8px;font-style:italic;line-height:14.5px}
.quotes .who{text-align:right;margin-top:3px}
.quotes .who b{color:var(--green-dark)}
.quotes hr{border:0;border-top:1px solid #ccc;margin:6px 0}
.qmark{font-size:46px;color:var(--green-light);opacity:.55;font-style:normal;font-family:'Roboto',sans-serif;line-height:1}
.footer{left:0;top:1119px;width:946px;height:81px;background:var(--footer)}
.footer-brand{left:132px;top:1137px;font-size:20px;font-weight:700;color:#e8e8e8;display:flex;align-items:center;gap:7px}
.footer-brand span{width:16px;height:16px;background:#e8e8e8}
.footer-tag{left:155px;top:1163px;font-size:9px;color:#ddd}
.footer-nav{right:131px;top:1135px;display:flex;gap:19px;font-size:9.5px;color:#eee}
.copy{right:131px;top:1166px;font-size:9.5px;color:#ddd}
</style>
</head>
<body>
<div class="abs green-band"></div>
<div class="abs page"></div>

<header>
  <div class="abs brand">
    <div class="brand-name"><span class="brand-mark"></span>MAPLECREST LEDGER</div>
    <div class="brand-tag">Plan Today, Rest Easy</div>
  </div>
  <div class="abs auth">SIGN UP &nbsp;|&nbsp; SIGN IN</div>
  <div class="abs social">
    <span style="background:#8a8a8a"></span>
    <span style="background:#8a8a8a"></span>
    <span style="background:#8a8a8a"></span>
  </div>
  <nav class="abs nav">
    <a class="active">HOME</a><a>ABOUT US</a><a>SERVICES</a><a>FEATURES</a><a>TESTIMONIALS</a><a style="padding-right:0">CONTACT US</a>
  </nav>
</header>

<section class="abs slider">
  <div class="slider-photo" role="img" aria-label="Smiling retired couple meeting with an advisor at a table"></div>
</section>
<div class="abs promo">
  <h2>SIGN UP</h2>
  <p><b>Only $19.99</b> For a One Year Membership</p>
  <p><b>Only $9.99</b> Per Year After That</p>
</div>
<div class="abs dots"><span></span><span></span><span></span><span></span></div>

<article class="abs card active" style="left:132px">
  <h3>IDENTIFY</h3>
  <div class="img" role="img" aria-label="Pen resting on banknotes and a financial chart" style="background:linear-gradient(135deg,#b9b59c,#eeeeea 60%,#9aa0a8)"></div>
  <p>Aliquam molestie, mi et imperdiet euismod, dui purus auctor tellus, et interdum lacus lectus et ante..</p>
  <a>LEARN MORE</a>
</article>
<article class="abs card" style="left:364px">
  <h3>PLAN</h3>
  <div class="img" role="img" aria-label="Reading glasses on a laptop keyboard" style="background:linear-gradient(160deg,#dcdcdc,#7a7a7a 55%,#2b2b2b)"></div>
  <p>Aliquam molestie, mi et imperdiet euismod, dui purus auctor tellus, et interdum lacus lectus et ante..</p>
  <a>LEARN MORE</a>
</article>
<article class="abs card" style="left:597px">
  <h3>RETIRE</h3>
  <div class="img" role="img" aria-label="Hammock on a sunny porch" style="background:linear-gradient(180deg,#9fc2e4,#d9c9a8 55%,#a88a5f)"></div>
  <p>Aliquam molestie, mi et imperdiet euismod, dui purus auctor tellus, et interdum lacus lectus et ante..</p>
  <a>LEARN MORE</a>
</article>

<div class="abs rule" style="top:655px"></div>

<section>
  <h2 class="abs section" style="left:132px;top:669px">WELCOME TO OUR WEBSITE</h2>
  <p class="abs welcome-text">Aliquam molestie, mi et imperdiet euismod, dui purus auctor tellus, et interdum lacus lectus et ante. Sed accumsan sollicitudin sapien, sit amet adipiscing turpis gravida ac. In congue, neque ac lobortis volutpat, libero mauris varius mi, vitae suscipit ipsum ligula vitae risus. Duis aliquam nibh a dui iaculis viverra id a velit. Vivamus egestas risus in magna varius commodo. Sed semper viverra egestas. Etiam pretium porttitor lectus, vel ornare neque porta volutpat.<br>Ut et scelerisque ante. Donec erat purus, faucibus vitae congue vel, porttitor nec lectus. Aenean a nibh eget turpis vehicula tempus ac sed massa. Vestibulum dolor nulla, ultrices ac tincidunt sed, laoreet non est.</p>
  <div class="abs btn" style="left:132px;top:862px">LEARN MORE</div>
</section>

<section>
  <h2 class="abs section" style="left:538px;top:669px">DEMO VIDEO</h2>
  <div class="abs video">
    <div class="abs video-frame" role="img" aria-label="Video still of glasses on a laptop keyboard"></div>
    <svg class="abs" style="left:120px;top:76px" width="36" height="36" viewBox="0 0 36 36"><circle cx="18" cy="18" r="17" fill="rgba(0,0,0,.55)" stroke="#fff" stroke-width="2"/><path d="M14 11 L25 18 L14 25Z" fill="#fff"/></svg>
    <div class="abs video-bar"></div>
  </div>
</section>

<div class="abs rule" style="top:908px"></div>

<section>
  <h2 class="abs section" style="left:132px;top:919px">FEATURES</h2>
  <ul class="abs features">
    <li><svg width="12" height="11" viewBox="0 0 12 11"><path d="M1 6 L4.5 9.5 L11 1.5" stroke="#2f7d1c" stroke-width="2.4" fill="none"/></svg>Identify and project your retirement needs and expectations including basic living expenses, housing costs, recreation, big ticket non-recurring items, medical and nursing home care.</li>
    <li><svg width="12" height="11" viewBox="0 0 12 11"><path d="M1 6 L4.5 9.5 L11 1.5" stroke="#2f7d1c" stroke-width="2.4" fill="none"/></svg>Identify and project all your sources of retirement income including retirement savings, other savings, pension plans, Social Security, life insurance and working part-time during retirement for a period of time.</li>
    <li><svg width="12" height="11" viewBox="0 0 12 11"><path d="M1 6 L4.5 9.5 L11 1.5" stroke="#2f7d1c" stroke-width="2.4" fill="none"/></svg>Strategize tapping into the equity of your real estate including swapping your primary residence for a different home or retirement area, or selling and renting.</li>
  </ul>
  <div class="abs btn" style="left:132px;top:1085px">LEARN MORE</div>
</section>

<section>
  <h2 class="abs section" style="left:596px;top:919px">TESTIMONIALS</h2>
  <div class="abs quotes">
    <span class="abs qmark" style="left:4px;top:-2px">&ldquo;</span>
    <p>This site is a great place to get a handle on your retirement strategy...</p>
    <p class="who"><b>- Dana</b>, Vermont</p>
    <hr>
    <p>I can see professionals using this site to validate their existing retirement plans...</p>
    <p class="who"><b>- Owen</b>, Vermont</p>
    <span class="abs qmark" style="right:4px;top:84px">&rdquo;</span>
  </div>
  <div class="abs btn" style="left:596px;top:1081px">READ ALL</div>
</section>

<footer>
  <div class="abs footer"></div>
  <div class="abs footer-brand"><span></span>MAPLECREST LEDGER</div>
  <div class="abs footer-tag">Plan Today, Rest Easy</div>
  <nav class="abs footer-nav"><span>HOME</span><span>ABOUT US</span><span>SERVICES</span><span>FEATURES</span><span>TESTIMONIALS</span><span>CONTACT US</span></nav>
  <div class="abs copy">Copyright © 2013. All Right Reserved &nbsp;|&nbsp; Privacy Policy &nbsp;|&nbsp; Terms &amp; Condition</div>
</footer>
</body>
</html>
```